Stress Coach website development

Need a website designed for a coaching business. Very high-end, luxury, professionalism, in the area of STRESS, see brief attached. I have a logo already
Updates

Slow in providing feedback

Target Market(s)

CEOs very successful men and wealthy females, high end luxury market

Industry/Entity Type

coaching

Number of Pages Required

1 page

Requirements
Must have
• Luxury look, professional, serious but warm, appealing to both sexes

```html
<!DOCTYPE html>
<html lang="en">
<head>
<meta charset="utf-8">
<title>CalmPath</title>
<link href="https://fonts.googleapis.com/css2?family=Roboto:wght@300;400;500;700&family=Montserrat:wght@400;600;700;800&display=swap" rel="stylesheet">
<style>
:root{
  --dark:#1f1f21;
  --dark-2:#2a2a2c;
  --yellow:#f4d21b;
  --blue:#2f6ea7;
  --blue-text:#2d7fc1;
  --pale-blue:#dcecf7;
  --grey-bg:#ececec;
  --text:#444;
  --white:#fff;
}
*{box-sizing:border-box;margin:0;padding:0}
html,body{width:1200px;height:3212px;overflow:hidden}
body{font-family:"Roboto",sans-serif;color:var(--text);background:var(--white);position:relative}
.header{height:56px;background:var(--dark);display:flex;align-items:center;justify-content:space-between;padding:0 40px}
.brand{color:var(--white);font-family:"Montserrat",sans-serif;font-weight:700;font-size:15px;letter-spacing:2px}
.nav{display:flex;gap:38px;font-size:14px;color:var(--white)}
.nav a{color:inherit;text-decoration:none;padding-bottom:6px}
.nav a.active{color:var(--yellow);border-bottom:2px solid var(--yellow)}
.hero{height:336px;background:linear-gradient(120deg,#3a6f8c,#5ea0b9 45%,#2f5a74);text-align:center;color:var(--white);display:flex;flex-direction:column;align-items:center;justify-content:center}
.hero .kicker{font-family:"Montserrat",sans-serif;font-size:34px;letter-spacing:8px;font-weight:600}
.hero .big{font-family:"Montserrat",sans-serif;font-size:82px;letter-spacing:14px;font-weight:800;color:var(--yellow);line-height:1}
.hero .sub{font-family:"Montserrat",sans-serif;font-size:26px;letter-spacing:7px;margin-top:4px}
.btn{display:inline-block;border:2px solid var(--yellow);border-radius:22px;padding:9px 30px;font-size:12px;letter-spacing:1px;text-transform:uppercase;color:var(--white);font-weight:500}
.btn-solid{background:var(--yellow);color:var(--dark);border-color:var(--yellow)}
.hero .btn{margin-top:26px;background:var(--yellow);color:var(--dark)}
.welcome{padding:60px 80px 0;height:668px}
.welcome h1{text-align:center;font-family:"Montserrat",sans-serif;font-size:40px;color:var(--dark);font-weight:700;margin-bottom:56px}
.welcome p{font-size:14px;line-height:1.75;margin-bottom:22px}
.coach{background:var(--grey-bg);height:500px;display:flex;padding:0 40px;align-items:stretch}
.coach-photo{width:552px;background:linear-gradient(160deg,#6b6b6b,#3d3d3d 60%,#8a8a8a)}
.coach-panel{flex:1;background:var(--dark-2);color:#ccc;padding:56px 52px}
.coach-panel h2{font-family:"Montserrat",sans-serif;color:var(--yellow);font-size:36px;margin-bottom:32px}
.coach-panel p{font-size:13px;line-height:1.7;margin-bottom:24px;max-width:470px}
.coach-panel .btn{margin-left:210px;margin-top:10px}
.courses{margin-top:24px;height:280px;background:var(--blue);display:flex;padding:0 40px}
.course{flex:1;border:1px solid rgba(255,255,255,.5);border-top:none;border-bottom:none;text-align:center;padding:50px 30px;color:var(--white)}
.course h3{font-size:21px;font-weight:700;line-height:1.25;margin-bottom:18px}
.course p{font-size:11px;opacity:.85;margin-bottom:28px}
.testimonials{text-align:center;padding-top:90px;height:626px}
.testimonials h2{font-family:"Montserrat",sans-serif;font-size:38px;color:var(--dark);margin-bottom:40px}
.avatar{width:96px;height:96px;border-radius:50%;margin:0 auto 38px;background:linear-gradient(#7a7a7a,#4b4b4b);border:3px solid #ddd}
.quote{font-size:23px;line-height:1.45;color:var(--blue-text);max-width:780px;margin:0 auto 30px;font-weight:300}
.client-name{color:var(--yellow);font-size:19px;margin-bottom:46px}
.dots{display:flex;gap:12px;justify-content:center}
.dots span{width:9px;height:9px;border-radius:50%;background:#ccc}
.dots span.on{background:var(--blue)}
.partners{height:80px;display:flex;align-items:center;justify-content:space-between;padding:0 110px}
.partner{display:flex;align-items:center;gap:8px;font-family:"Montserrat",sans-serif;font-weight:700;font-size:17px;color:#3a3a3a}
.partner i{width:16px;height:16px;background:#3a3a3a;display:block}
.cta-strip{height:72px;background:var(--pale-blue);display:flex;align-items:center;justify-content:center;font-size:22px;color:var(--blue-text);font-weight:500}
.footer{position:absolute;left:0;top:2640px;width:1200px;height:572px;background:var(--dark);color:#bbb;display:flex;gap:60px;padding:60px 40px}
.footer h4{color:var(--white);font-size:21px;margin-bottom:34px;font-weight:700}
.col{flex:1}
.links li{list-style:none;color:var(--yellow);font-size:14px;font-weight:500;margin-bottom:22px;text-transform:uppercase}
.small{font-size:11px;line-height:1.6;margin-bottom:18px}
.field{height:24px;background:var(--white);margin-bottom:14px;border-radius:2px}
.field.tall{height:84px}
.footer .btn{padding:8px 34px;color:var(--dark)}
.socials{display:flex;gap:14px;justify-content:center;margin-top:40px}
.socials span{width:36px;height:36px;border-radius:50%;background:var(--white)}
</style>
</head>
<body>
<header class="header">
  <div class="brand">CALMPATH</div>
  <nav class="nav"><a class="active">Why me ?</a><a>Meet the Coach</a><a>Programs</a><a>Testimonials</a><a>Contact</a></nav>
</header>

<section class="hero" role="img" aria-label="Group of smiling people lying in a circle, heads together">
  <div class="kicker">LEARN TO SET YOUR</div>
  <div class="big">STRESS</div>
  <div class="sub">REDUCTION GOALS</div>
  <span class="btn">Contact me</span>
</section>

<section class="welcome">
  <h1>Welcome to CalmPath</h1>
  <p>CalmPath came about due to my desire to help people lead a better and healthier life. Initially, I was involved in the world of health. For years I practised ways to ease tension, and I noticed how important the mind is to lasting wellness, and that the mind is both powerful and controlling. Control the mind, control the body and achieve success. Stress can be the most debilitating factor in our lives, it is the root cause of so many illnesses and costs companies millions of dollars a year in lost productivity.</p>
  <p>However, stress is not all bad, we need stress to survive and perform at an optimal level. In order to do that, you need to recognise your stressors and then control them, and you will see your life change. Stress is not all bad, and once you are surrounded by calm, you will be working at your best, able to lead with clarity and confidence in every room you enter.</p>
  <p>Recognise when we are feeling stress and what is causing it, understand it and how we react to it is the first step. Then when we sense it coming we can deal with it calmly, or use it to our advantage. Effective stress control and problem solving skills may be the one thing that will keep you ahead when others falter under pressure. It really is knowing which tools to use and when. What is your plan for the next decade? Let us build it together.</p>
</section>

<section class="coach">
  <div class="coach-photo" role="img" aria-label="Portrait of the coach holding a coffee cup outdoors"></div>
  <div class="coach-panel">
    <h2>The CalmPath Coach</h2>
    <p>Born then raised, I have been through a lot: started businesses, sold companies, ran teams, sat on boards, travelled widely and learned what pressure truly does to a person. I have faced it head on and found calm on the other side, and now I share the good lessons with you.</p>
    <p>Limited number of clients, different stage of life, simply better. Have a full calm, and I will guide you there.</p>
    <span class="btn">Share your stress</span>
  </div>
</section>

<section class="courses">
  <div class="course"><h3>Stress Management<br>Course for Individuals</h3><p>Learn to see stress and develop calm habits</p><span class="btn btn-solid">Contact us</span></div>
  <div class="course"><h3>Stress Reduction<br>Course for Organization</h3><p>Give the gift of stress relief to your teams and members</p><span class="btn btn-solid">Contact us</span></div>
  <div class="course"><h3>Stress Reduction<br>Course for Family</h3><p>Stress relief programs for loved ones and couples</p><span class="btn btn-solid">Contact us</span></div>
</section>

<section class="testimonials">
  <h2>Our Client Says</h2>
  <div class="avatar" role="img" aria-label="Client portrait"></div>
  <p class="quote">In enim justo, rhoncus ut, imperdiet a, venenatis vitae, justo. Nullam dictum felis eu pede mollis pretium. Integer tincidunt. Cras dapibus. Vivamus elementum semper nisi. Aenean vulputate eleifend tellus.</p>
  <div class="client-name">Daniel Moreau</div>
  <div class="dots"><span></span><span class="on"></span><span></span><span></span></div>
</section>

<section class="partners">
  <div class="partner"><i></i>Harborline Health</div>
  <div class="partner">Summit Guild</div>
  <div class="partner">Corvane</div>
  <div class="partner">Meridian Circle</div>
  <div class="partner">Alderpoint</div>
  <div class="partner"><i></i>Westvale University</div>
</section>

<section class="cta-strip">Tell us about you and your stress reduction goals for your workplace, school or organization.</section>

<footer class="footer">
  <div class="col">
    <h4>Quick Links</h4>
    <ul class="links">
      <li>Stress course for individuals</li>
      <li>Family stress course programs</li>
      <li>Courses for organization</li>
      <li>Online courses</li>
      <li>Terms &amp; conditions</li>
      <li>Privacy policy</li>
    </ul>
  </div>
  <div class="col">
    <h4>Share Your Stress</h4>
    <p class="small">Share your stress and we will send advice right back to your workplace, school or organisation.</p>
    <p class="small">Your details stay private and are never shared with anyone else.</p>
    <div class="field"></div><div class="field"></div><div class="field"></div><div class="field tall"></div>
    <span class="btn btn-solid">Submit</span>
  </div>
  <div class="col">
    <h4>More Information</h4>
    <p class="small">Please subscribe to get our calm information about our latest courses, resources, news and more.</p>
    <div class="field"></div>
    <p class="small">By subscribing you agree to receive our monthly letter and accept the terms and privacy policy of the site.</p>
    <span class="btn btn-solid" style="display:block;text-align:center">Subscribe</span>
    <div class="socials"><span></span><span></span><span></span><span></span></div>
  </div>
</footer>
</body>
</html>
```